Invoice design

Please design an invoice like the attached

- Please include a logo in the header (any logo rectangular is fine)

- We do not need a DUE DATE on the invoice (next to the total inc. vat)

- For each product put in smaller text beneath which might contain additional information about the product (e.g. size, colour choices)

- Do not put a signature in the footer

```html
<!DOCTYPE html>
<html lang="en">
<head>
<meta charset="utf-8">
<title>Invoice 00001 – Northgate Ltd</title>
<link href="https://fonts.googleapis.com/css2?family=Jost:wght@400;500;600;700;800&display=swap" rel="stylesheet">
<style>
  :root {
    --accent: #b5937e;
    --ink: #4a4a4a;
    --ink-soft: #5a5a5a;
    --rule-light: #dcdcdc;
    --footer-bg: #e6e6e6;
    --footer-rule: #d0d0d0;
    --paper: #ffffff;
  }
  * { margin: 0; padding: 0; box-sizing: border-box; }
  html, body { width: 813px; height: 1200px; overflow: hidden; background: var(--paper); }
  body { font-family: "Jost", sans-serif; color: var(--ink); position: relative; }
  .abs { position: absolute; line-height: 1; white-space: nowrap; }

  .top-band { position: absolute; left: 0; top: 0; width: 813px; height: 22px; background: var(--accent); }
  .brand { left: 540px; top: 46px; font-size: 50px; font-weight: 600; color: var(--ink); letter-spacing: -1px; }

  .title { left: 64px; top: 106px; font-size: 52px; font-weight: 700; color: var(--accent); letter-spacing: 1px; }
  .meta-label { font-size: 14px; font-weight: 500; color: var(--accent); left: 67px; }
  .meta-value { font-size: 15px; font-weight: 500; color: var(--ink); left: 67px; }

  .divider-v { position: absolute; left: 310px; top: 108px; width: 1px; height: 296px; background: var(--accent); }

  .party { position: absolute; left: 339px; font-size: 13.5px; line-height: 18px; color: var(--ink); }
  .party h2 { font-size: 13.5px; font-weight: 500; color: var(--accent); }
  .party .name { font-weight: 500; }

  .th { top: 478px; font-size: 15px; font-weight: 500; color: var(--accent); }
  .table-rule { position: absolute; left: 67px; width: 677px; top: 505px; height: 2px; background: var(--accent); }
  .row-rule { position: absolute; left: 67px; width: 677px; height: 2px; background: var(--rule-light); }
  .item-name { left: 67px; font-size: 14px; font-weight: 500; color: var(--ink); }
  .cell { font-size: 13px; color: var(--ink); }
  .num { text-align: right; }
  .spec { font-size: 9.5px; color: var(--ink-soft); }

  .sum-label { left: 434px; font-size: 13px; font-weight: 500; color: var(--accent); }
  .sum-value { right: 69px; font-size: 15px; color: var(--ink); text-align: right; }
  .sum-rule { position: absolute; left: 434px; width: 310px; height: 1px; background: var(--accent); }
  .grand-box { position: absolute; left: 414px; top: 800px; width: 348px; height: 50px; border: 1px dashed var(--accent); }
  .grand-amount { right: 70px; top: 809px; font-size: 31px; font-weight: 800; color: var(--accent); }

  .footer { position: absolute; left: 0; top: 872px; width: 813px; height: 328px; background: var(--footer-bg); }
  .notch { position: absolute; left: 392px; top: 872px; }
  .pay-rule { position: absolute; left: 569px; top: 911px; width: 2px; height: 145px; background: var(--footer-rule); }
  .pay-label { left: 589px; font-size: 13px; font-weight: 500; color: var(--accent); }
  .pay-value { left: 589px; font-size: 13px; color: var(--ink); }
  .foot-rule { position: absolute; left: 59px; top: 1093px; width: 679px; height: 2px; background: var(--footer-rule); }
  .foot-line { left: 0; width: 813px; text-align: center; font-size: 11px; color: var(--ink-soft); }
</style>
</head>
<body>
  <div class="top-band"></div>
  <div class="abs brand">Halden</div>

  <h1 class="abs title">INVOICE</h1>
  <div class="abs meta-label" style="top:180px">INVOICE:</div>
  <div class="abs meta-value" style="top:199px">00001</div>
  <div class="abs meta-label" style="top:229px">ISSUE DATE:</div>
  <div class="abs meta-value" style="top:248px">July 3, 2020</div>
  <div class="abs meta-label" style="top:278px">DELIVERY DATE:</div>
  <div class="abs meta-value" style="top:298px">July 3, 2020</div>
  <div class="abs meta-label" style="top:328px">DUE DATE:</div>
  <div class="abs meta-value" style="top:347px">July 18, 2020</div>

  <div class="divider-v"></div>

  <section class="party" style="top:108px">
    <h2>SUPPLIER</h2>
    <div class="name">Northgate Ltd</div>
    <div>42 Farrow Lane</div>
    <div>London</div>
    <div>EC1V 4PW</div>
    <div>United Kingdom</div>
    <div>VAT No: GB4817302256</div>
  </section>

  <section class="party" style="top:260px">
    <h2>CLIENT</h2>
    <div class="name">Martin Ellery</div>
    <div>The Copper Kettle</div>
    <div>17 Holloway Mews</div>
    <div>London</div>
    <div>N7 6QT</div>
    <div>United Kingdom</div>
    <div>VAT No: GB456 7788 21</div>
  </section>

  <div class="abs th" style="left:67px">Item</div>
  <div class="abs th" style="left:293px">Description</div>
  <div class="abs th" style="left:404px">Quantity</div>
  <div class="abs th" style="left:512px">Unit Price Incl. VAT</div>
  <div class="abs th" style="left:655px">VAT</div>
  <div class="abs th num" style="right:69px">Total</div>
  <div class="table-rule"></div>

  <div class="abs item-name" style="top:520px">Highland Ridge Reserve</div>
  <div class="abs cell" style="left:295px;top:521px">1 kg / Full City</div>
  <div class="abs cell" style="left:428px;top:521px">2</div>
  <div class="abs cell num" style="right:180px;top:521px">15.00</div>
  <div class="abs cell" style="left:656px;top:521px">20%</div>
  <div class="abs cell num" style="right:68px;top:521px">£30.00</div>
  <div class="abs spec" style="left:67px;top:542px">Size&nbsp;&nbsp;&nbsp;&nbsp;&nbsp;: 50 cm</div>
  <div class="abs spec" style="left:172px;top:542px">Text 3&nbsp;&nbsp;: Answer 3</div>
  <div class="abs spec" style="left:67px;top:555px">Color&nbsp;&nbsp;&nbsp;: Light Brown</div>
  <div class="abs spec" style="left:172px;top:555px">Text 4&nbsp;&nbsp;: Answer 4</div>
  <div class="row-rule" style="top:571px"></div>

  <div class="abs item-name" style="top:579px">Highland Ridge Reserve</div>
  <div class="abs cell" style="left:295px;top:580px">1 kg / Full City</div>
  <div class="abs cell" style="left:428px;top:580px">3</div>
  <div class="abs cell num" style="right:180px;top:580px">65.00</div>
  <div class="abs cell" style="left:656px;top:580px">20%</div>
  <div class="abs cell num" style="right:68px;top:580px">£195.00</div>
  <div class="abs spec" style="left:67px;top:600px">Size&nbsp;&nbsp;&nbsp;&nbsp;&nbsp;: 20 m</div>
  <div class="abs spec" style="left:172px;top:600px">Text 3&nbsp;&nbsp;: Answer 3</div>
  <div class="abs spec" style="left:67px;top:613px">Color&nbsp;&nbsp;&nbsp;: Sky Blue</div>
  <div class="abs spec" style="left:172px;top:613px">Text 4&nbsp;&nbsp;: Answer 4</div>
  <div class="row-rule" style="top:629px"></div>

  <div class="abs sum-label" style="top:646px">SUBTOTAL:</div>
  <div class="abs sum-value" style="top:644px">£223.00</div>
  <div class="sum-rule" style="top:672px"></div>
  <div class="abs sum-label" style="top:687px">SHIPPING:</div>
  <div class="abs sum-value" style="top:685px">£18.00</div>
  <div class="sum-rule" style="top:714px"></div>
  <div class="abs sum-label" style="top:728px">TOTAL EXCL. VAT:</div>
  <div class="abs sum-value" style="top:726px">£205.50</div>
  <div class="sum-rule" style="top:756px"></div>
  <div class="abs sum-label" style="top:770px">VAT 20%:</div>
  <div class="abs sum-value" style="top:768px">£37.50</div>

  <div class="grand-box"></div>
  <div class="abs sum-label" style="top:821px">TOTAL INCL. VAT:</div>
  <div class="abs grand-amount">£243.00</div>

  <footer class="footer"></footer>
  <svg class="notch" width="28" height="13" viewBox="0 0 28 13" aria-hidden="true">
    <polygon points="0,0 28,0 14,13" fill="#ffffff"/>
  </svg>

  <div class="pay-rule"></div>
  <div class="abs pay-label" style="top:917px">PAYMENT&nbsp; METHOD</div>
  <div class="abs pay-value" style="top:937px">Bank Transfer</div>
  <div class="abs pay-label" style="top:969px">BANK ACCOUNT</div>
  <div class="abs pay-value" style="top:989px">5120&nbsp; 0000&nbsp; 0348&nbsp; 2961</div>
  <div class="abs pay-label" style="top:1021px">ORDER NUMBER</div>
  <div class="abs pay-value" style="top:1041px">#1029</div>

  <div class="foot-rule"></div>
  <div class="abs foot-line" style="top:1116px">Northgate Ltd&nbsp; | &nbsp;Phone: +44 1632 960842&nbsp; | &nbsp;Email: hello@northgate.co.uk&nbsp; | &nbsp;Website: northgate.co.uk&nbsp; | &nbsp;Social: social.example/northgate</div>
  <div class="abs foot-line" style="top:1141px">View this document online at https://docs.northgate.co.uk/r7kq2m9x. Created in Ledgerly</div>
</body>
</html>
```